Business Card Design for Brindle Tech Hub

need a business card designed around my business which services the technological aspects. needs to look techi but not over the top

PC / MAC Repairs Sales, Service And Custom Builds
Internet / Wifi Issues
Networking
TV Mounting
Hifi Setup

Other Services On Demand

(doesn't have to be this wording but needs to include services that i provide)

ABN: 47 203 618 952
Find Us on Facebook Logo
Ph 0417283905
Simon Palfrey
Owner / Director
Email simon@brindletechhub.com

Industry/Entity Type

Technical Service

```html
<!DOCTYPE html>
<html lang="en">
<head>
<meta charset="utf-8">
<title>Brindle Tech Hub – Business Card</title>
<link rel="stylesheet" href="https://fonts.googleapis.com/css2?family=Montserrat:wght@400;500;600;800&display=swap">
<style>
  :root {
    --navy: #13265a;
    --sky: #3aa3e0;
    --sky-deep: #2b7cc4;
    --paper: #ffffff;
    --stage: #e4e4e4;
    --ink: #1d2a4d;
  }
  * { box-sizing: border-box; margin: 0; padding: 0; }
  html, body { width: 1200px; height: 852px; overflow: hidden; }
  body {
    background: var(--stage);
    font-family: "Montserrat", Arial, sans-serif;
    position: relative;
  }
  .card {
    position: absolute;
    width: 540px;
    height: 310px;
    background: var(--paper);
    border-radius: 20px;
    overflow: hidden;
    box-shadow: 0 6px 18px rgba(0,0,0,0.12);
  }
  .card--front { left: 50px; top: 110px; }
  .card--back  { left: 610px; top: 430px; }

  .brand {
    display: flex;
    align-items: center;
    gap: 10px;
    color: var(--navy);
    font-weight: 800;
    font-size: 34px;
    letter-spacing: 0.5px;
    text-transform: uppercase;
    line-height: 1;
    white-space: nowrap;
  }
  .brand__dot {
    width: 16px; height: 16px;
    border-radius: 50%;
    background: var(--sky);
    flex: none;
  }

  /* front */
  .card--front .brand { position: absolute; left: 60px; top: 62px; }
  .services-band {
    position: absolute;
    left: 0; right: 0;
    top: 120px; height: 112px;
    background: linear-gradient(90deg, var(--sky-deep) 0%, var(--navy) 55%, var(--navy) 100%);
    color: #fff;
    display: flex;
    flex-direction: column;
    justify-content: center;
    align-items: center;
    gap: 6px;
    font-size: 14px;
    font-weight: 500;
    text-align: center;
  }
  .front-footer {
    position: absolute;
    left: 0; right: 0; top: 254px;
    display: flex;
    justify-content: center;
    align-items: center;
    gap: 8px;
    font-size: 13px;
    color: var(--ink);
    font-weight: 500;
  }
  .social-dot {
    display: inline-block;
    width: 13px; height: 13px;
    border-radius: 50%;
    background: var(--sky);
    flex: none;
  }

  /* back */
  .card--back .brand { position: absolute; left: 36px; top: 48px; font-size: 31px; }
  .contact {
    position: absolute;
    left: 316px; top: 104px;
    font-size: 12.5px;
    color: var(--ink);
    display: flex;
    flex-direction: column;
    gap: 4px;
    white-space: nowrap;
  }
  .contact__row { display: flex; align-items: center; gap: 8px; line-height: 16px; }
  .contact__row svg { width: 13px; height: 13px; flex: none; fill: var(--navy); }
  .web-accent { color: var(--sky); }
  .person {
    position: absolute;
    left: 36px; top: 228px;
  }
  .person__name { font-size: 20px; font-weight: 600; color: var(--navy); }
  .person__role { font-size: 12px; color: var(--sky); margin-top: 2px; }
  .back-strip {
    position: absolute; left: 0; top: 0;
    width: 100%; height: 310px;
  }
  .abn {
    position: absolute;
    right: 30px; top: 216px;
    color: #fff;
    font-size: 12.5px;
    font-weight: 500;
  }
</style>
</head>
<body>

<section class="card card--front" aria-label="Business card front">
  <div class="brand"><span class="brand__dot"></span>Brindle Tech Hub</div>
  <div class="services-band">
    <p>PC / MAC Repairs Sales and Service and custom builds</p>
    <p>Internet / Wifi Issues &nbsp;|&nbsp; Networking &nbsp;|&nbsp; TV Mounting &nbsp;|&nbsp; Hifi Setup</p>
    <p>Other services on demand</p>
  </div>
  <div class="front-footer">
    <span>Find us on</span><span class="social-dot"></span>
    <span>|</span><span>www.brindletechhub.com</span>
  </div>
</section>

<section class="card card--back" aria-label="Business card back">
  <svg class="back-strip" viewBox="0 0 540 310" preserveAspectRatio="none" aria-hidden="true">
    <polygon points="0,292 420,268 540,268 540,310 0,310" fill="#3aa3e0"/>
    <path d="M400,198 L540,198 L540,310 L372,310 L372,226 Q372,198 400,198 Z" fill="#13265a"/>
  </svg>

  <div class="brand"><span class="brand__dot"></span>Brindle Tech Hub</div>

  <div class="contact">
    <div class="contact__row"><span>Find us on</span><span class="social-dot"></span></div>
    <div class="contact__row">
      <svg viewBox="0 0 24 24"><path d="M6.6 10.8a15.1 15.1 0 0 0 6.6 6.6l2.2-2.2a1 1 0 0 1 1-.25 11.4 11.4 0 0 0 3.6.57 1 1 0 0 1 1 1V20a1 1 0 0 1-1 1A17 17 0 0 1 3 4a1 1 0 0 1 1-1h3.5a1 1 0 0 1 1 1c0 1.25.2 2.45.57 3.57a1 1 0 0 1-.25 1z"/></svg>
      <span>0417283905</span>
    </div>
    <div class="contact__row">
      <svg viewBox="0 0 24 24"><path d="M2 5h20v14H2z M2 5l10 8 10-8" fill="none" stroke="#13265a" stroke-width="2"/></svg>
      <span>simon@brindletechhub.com</span>
    </div>
    <div class="contact__row">
      <svg viewBox="0 0 24 24"><circle cx="12" cy="12" r="9" fill="none" stroke="#13265a" stroke-width="2"/><path d="M3 12h18M12 3c3 3 3 15 0 18M12 3c-3 3-3 15 0 18" fill="none" stroke="#13265a" stroke-width="1.6"/></svg>
      <span>www.<span class="web-accent">brindletechhub</span>.com</span>
    </div>
  </div>

  <div class="person">
    <p class="person__name">Simon Palfrey</p>
    <p class="person__role">Owner / Director</p>
  </div>

  <p class="abn">ABN: 47 203 618 952</p>
</section>

</body>
</html>
```